We want a hot New Design for our IT company Web Site

We have a basic website with some general information and lots of mostly words and generic pictures we want to make it look and feel a lot more modern and slick. The site needs to work on mobile devices as well as desktops.

Target Market(s)

Business customers

Industry/Entity Type

It Company

Coding

Coded - Design and coding required

Number of Pages Required

5+ page

Requirements
Must have
• Sleek new Design making it look and feel more modern and less boring
Nice to have
• If it can have a better flow to it rather then have the std Drop down menus it has now.

```html
<!DOCTYPE html>
<html lang="en">
<head>
<meta charset="utf-8">
<title>K &amp; R Solutions Group</title>
<link href="https://fonts.googleapis.com/css2?family=Open+Sans:wght@400;600;700;800&display=swap" rel="stylesheet">
<style>
:root{
  --blue:#1a5fae;
  --blue-dark:#0f3f78;
  --navy:#0d1b2e;
  --ink:#222;
  --muted:#666;
  --grey:#e6e6e6;
  --footer:#2b2b2b;
  --footer-dark:#1c1c1c;
  --white:#fff;
}
*{box-sizing:border-box;margin:0;padding:0}
html,body{width:758px;height:1200px;overflow:hidden;background:var(--white);font-family:"Open Sans",Arial,sans-serif;color:var(--ink)}
.page{width:758px;height:1200px;position:relative}
.site-header{height:62px;display:flex;align-items:center;justify-content:space-between;padding:0 30px 0 80px}
.brand{display:flex;align-items:center;gap:8px;color:var(--blue);font-weight:800;font-size:18px}
.brand-square{width:22px;height:22px;background:var(--blue)}
.brand small{display:block;font-size:9px;font-weight:700;letter-spacing:1px}
.header-phone{display:flex;align-items:center;gap:6px;font-size:13px;font-weight:700;color:var(--ink)}
.main-nav{height:24px;background:var(--blue);display:flex;align-items:center;padding-left:84px;gap:16px}
.main-nav a{color:var(--white);font-size:8px;font-weight:700;text-decoration:none;text-transform:uppercase}
.main-nav a.active{background:var(--blue-dark);padding:7px 8px}
.hero{height:258px;position:relative;background:linear-gradient(120deg,#0b2448 0%,#1d5c9a 45%,#8fb6d8 70%,#2a5f93 100%)}
.hero-caption{position:absolute;left:78px;top:98px;width:205px;background:rgba(10,20,35,.72);padding:8px 12px;color:var(--white);font-size:20px;font-weight:700;line-height:1.2}
.services{height:175px;display:flex;justify-content:center;gap:62px;padding-top:22px}
.service{width:95px;text-align:center}
.service-icon{width:60px;height:60px;border-radius:50%;background:#2b2b2b;border:4px solid #cfcfcf;margin:0 auto 10px;display:flex;align-items:center;justify-content:center}
.service-title{color:var(--blue);font-size:9px;font-weight:700;text-transform:uppercase;line-height:1.3}
.about{height:180px;background:var(--grey);padding:28px 80px 0;text-align:center}
.section-title{display:flex;align-items:center;gap:8px;font-size:14px;font-weight:700;text-transform:uppercase;color:var(--ink)}
.section-title span{color:var(--blue)}
.about .section-title{justify-content:center}
.mark{width:16px;height:12px;background:var(--blue)}
.about p{font-size:8px;color:var(--muted);line-height:1.55;margin-top:16px;text-align:left}
.btn{display:inline-block;background:var(--blue);color:var(--white);font-size:8px;font-weight:700;padding:5px 10px;margin-top:14px}
.split{display:flex;gap:20px;padding:18px 80px 0;height:275px}
.split>section{flex:1}
.contact p,.latest p{font-size:7px;color:var(--muted);margin:8px 0}
.form-row{display:flex;gap:8px;margin-bottom:6px}
.field{flex:1;height:14px;border:1px solid #ccc;font-size:6px;color:#999;padding:3px 4px}
.field.msg{height:40px}
.form-actions{text-align:right}
.form-actions .btn{margin-top:4px}
.latest-head{display:flex;justify-content:space-between;align-items:center}
.arrows{color:#999;font-size:10px}
.post{display:flex;gap:8px;margin-top:10px}
.post-thumb{width:30px;height:28px;background:linear-gradient(135deg,#5a6e84,#a7b4c2)}
.post h4{font-size:7px;font-weight:700;display:flex;justify-content:space-between;width:206px}
.post h4 time{color:var(--muted);font-weight:600}
.post p{margin:2px 0 0}
.site-footer{position:absolute;top:975px;left:0;width:758px;height:225px;background:var(--footer);color:#ccc}
.footer-cols{display:flex;padding:10px 80px 0;gap:20px}
.footer-cols h5{font-size:8px;color:var(--white);margin-bottom:10px}
.quick{width:100px}
.quick li{list-style:none;font-size:7px;line-height:1.5}
.testi{width:130px}
.testi-photo{width:30px;height:30px;border-radius:50%;background:#6c7a88;margin:0 auto 6px}
.quote{background:var(--blue);color:var(--white);font-size:7px;padding:6px;line-height:1.4}
.info{width:150px;font-size:7px}
.info h5{display:flex;justify-content:space-between}
.socials{display:flex;gap:4px}
.socials i{width:10px;height:10px;border-radius:50%;background:var(--blue);display:block}
.info-line{display:flex;gap:6px;margin-bottom:10px;line-height:1.4}
.info-line b{color:var(--white)}
.footer-brand{flex:1;text-align:center;color:var(--white);font-weight:800;font-size:20px;padding-top:18px}
.footer-brand small{display:block;font-size:6px;font-weight:400;color:#aaa;margin-top:8px}
.footer-bar{position:absolute;bottom:0;left:0;width:100%;height:26px;background:var(--footer-dark)}
</style>
</head>
<body>
<div class="page">
  <header class="site-header">
    <div class="brand"><div class="brand-square"></div><div>K &amp; R<small>SOLUTIONS GROUP</small></div></div>
    <div class="header-phone">
      <svg width="14" height="14" viewBox="0 0 24 24"><circle cx="12" cy="12" r="12" fill="#222"/><path d="M8 6l2 0 1 3-1.5 1a7 7 0 0 0 4 4l1-1.5 3 1v2c0 1-1 1.5-2 1.5A11 11 0 0 1 6.5 8C6.5 7 7 6 8 6z" fill="#fff"/></svg>
      1300 555 010
    </div>
  </header>
  <nav class="main-nav">
    <a class="active" href="#">Home</a><a href="#">Consult</a><a href="#">Provide</a><a href="#">Provision</a><a href="#">Cloud &amp; Connectivity</a><a href="#">Software Development</a><a href="#">Blog</a><a href="#">Contact Us</a>
  </nav>
  <section class="hero" role="img" aria-label="Photo of a hand touching a glowing cloud network linked to devices">
    <h1 class="hero-caption">We are a new IT Managed Services Provider</h1>
  </section>
  <section class="services">
    <div class="service"><div class="service-icon"><svg width="26" height="26" viewBox="0 0 24 24" fill="none" stroke="#fff" stroke-width="2"><circle cx="9" cy="8" r="3"/><circle cx="16" cy="9" r="2.5"/><path d="M3 20c0-4 3-6 6-6s6 2 6 6M14 14c3 0 6 2 6 5"/></svg></div><div class="service-title">Technology Consulting</div></div>
    <div class="service"><div class="service-icon"><svg width="26" height="26" viewBox="0 0 24 24" fill="none" stroke="#fff" stroke-width="2"><rect x="4" y="4" width="16" height="12"/><path d="M8 20h8M12 16v4"/></svg></div><div class="service-title">Managed IT Services</div></div>
    <div class="service"><div class="service-icon"><svg width="26" height="26" viewBox="0 0 24 24" fill="none" stroke="#fff" stroke-width="2"><path d="M7 17a4 4 0 0 1 0-8 5 5 0 0 1 10 1 3.5 3.5 0 0 1 0 7z"/></svg></div><div class="service-title">Cloud Services &amp; Hosting</div></div>
    <div class="service"><div class="service-icon"><svg width="26" height="26" viewBox="0 0 24 24" fill="none" stroke="#fff" stroke-width="2"><rect x="3" y="5" width="18" height="12"/><path d="M9 9l-3 2 3 2M15 9l3 2-3 2"/></svg></div><div class="service-title">Software Development</div></div>
  </section>
  <section class="about">
    <h2 class="section-title"><i class="mark"></i>About <span>K &amp; R Solutions Group</span></h2>
    <p>We are a team of IT specialists who help businesses plan, build and run reliable technology. From managed support to cloud services and custom software, we deliver clear advice, fast response and systems that grow with you. Talk to us about your next project today.</p>
    <a class="btn" href="#">Read More ▸</a>
  </section>
  <div class="split">
    <section class="contact">
      <h2 class="section-title"><svg width="14" height="14" viewBox="0 0 24 24"><path d="M2 12l20-9-6 18-4-7z" fill="#222"/></svg>Get in <span>Touch with us</span></h2>
      <p>Send us a short note and our team will reply within one business day.</p>
      <div class="form-row"><div class="field">First Name</div><div class="field">Last Name</div></div>
      <div class="form-row"><div class="field">Phone Number</div><div class="field">Email</div></div>
      <div class="form-row"><div class="field msg">Your Message</div></div>
      <div class="form-actions"><a class="btn" href="#">SUBMIT</a></div>
    </section>
    <section class="latest">
      <div class="latest-head"><h2 class="section-title"><svg width="14" height="14" viewBox="0 0 24 24"><rect x="3" y="3" width="18" height="18" fill="#222"/><path d="M7 8h10M7 12h10M7 16h6" stroke="#fff" stroke-width="2"/></svg>Latest <span>Blog</span></h2><span class="arrows">‹ ›</span></div>
      <article class="post"><div class="post-thumb" role="img" aria-label="Author photo"></div><div><h4>Cloud backup tips for small firms <time>06 AUG, 2015</time></h4><p>Simple steps to keep your business data safe and ready.</p></div></article>
      <article class="post"><div class="post-thumb" role="img" aria-label="Author photo"></div><div><h4>Cloud backup tips for small firms <time>06 AUG, 2015</time></h4><p>Simple steps to keep your business data safe and ready.</p></div></article>
      <article class="post"><div class="post-thumb" role="img" aria-label="Author photo"></div><div><h4>Cloud backup tips for small firms <time>06 AUG, 2015</time></h4><p>Simple steps to keep your business data safe and ready.</p></div></article>
    </section>
  </div>
  <footer class="site-footer">
    <div class="footer-cols">
      <div class="quick"><h5>Quick Links</h5><ul><li>Home</li><li>Consult</li><li>Provide</li><li>Provision</li><li>Cloud &amp; Connectivity</li><li>Software Development</li><li>Blog</li><li>Contact Us</li></ul></div>
      <div class="testi"><h5>Client Testimonials</h5><div class="testi-photo" role="img" aria-label="Client portrait"></div><div class="quote"><b>Alex Morgan</b><br>Fast support and clear advice. Our network has never run better.</div></div>
      <div class="info"><h5>Contact Info <span class="socials"><i></i><i></i><i></i><i></i></span></h5>
        <div class="info-line"><svg width="10" height="12" viewBox="0 0 24 24"><path d="M12 2a7 7 0 0 0-7 7c0 5 7 13 7 13s7-8 7-13a7 7 0 0 0-7-7z" fill="#1a5fae"/></svg><span>Level 2, 18 Harbour Lane,<br>Newtown, QLD 4000</span></div>
        <div class="info-line"><svg width="10" height="10" viewBox="0 0 24 24"><circle cx="12" cy="12" r="12" fill="#1a5fae"/></svg><b>1300 555 010</b></div>
        <div class="info-line"><svg width="10" height="10" viewBox="0 0 24 24"><rect x="2" y="5" width="20" height="14" fill="#1a5fae"/></svg><span>hello@krsolutions.example</span></div>
      </div>
      <div class="footer-brand">K &amp; R<small>2015 K &amp; R Solutions Group<br>All Rights Reserved</small></div>
    </div>
    <div class="footer-bar"></div>
  </footer>
</div>
</body>
</html>
```